design a business card for a small company

Please design a business card with a black background. I have included a sample design, and you can try to emulate this. However, the logo should have different colors. Look at the picture [login to view URL]: the logo should have two colors as in this example. The VEK part should have the color of aluminium and the 842 AS part should have the color of stainless steel. Feel free to experiment.

Please use a high-def logo for your design.

The cards should be set up for the following text:

Name
Job title
Email address
Phone number
Company Name
Company address

Remember to create both front and back designs!

```html
<!DOCTYPE html>
<html lang="en">
<head>
<meta charset="UTF-8">
<title>VEK 842 AS — Business Card</title>
<link rel="stylesheet" href="https://fonts.googleapis.com/css2?family=Lato:wght@400;700&display=swap">
<style>
  :root {
    --page: #ece9e4;
    --card: #0d0b0b;
    --ink: #f4f1ee;
    --ink-soft: #dcd6d0;
    --metal: #d8c2b2;
    --rule-warm: #b88f6f;
    --rule-dark: #3a3533;
  }
  * { margin: 0; padding: 0; box-sizing: border-box; }
  html, body {
    width: 1200px; height: 1200px; overflow: hidden;
    background: var(--page);
    font-family: "Lato", sans-serif;
  }
  .canvas { position: relative; width: 1200px; height: 1200px; }

  .card {
    position: absolute; left: 223px; width: 753px; height: 425px;
    background: var(--card); border-radius: 18px; color: var(--ink);
  }
  .card--front { top: 144px; }
  .card--back { top: 635px; }

  .wordmark {
    position: absolute; color: var(--metal);
    font-family: "Lato", sans-serif; font-weight: 700;
    letter-spacing: 1px; white-space: nowrap;
  }
  .card--front .wordmark { left: 62px; top: 182px; font-size: 46px; }
  .card--back .wordmark { left: 0; right: 0; top: 152px; text-align: center; font-size: 62px; }

  .divider {
    position: absolute; left: 384px; top: 136px; width: 2px; height: 160px;
    background: var(--rule-dark);
  }
  .contact { position: absolute; left: 411px; top: 126px; width: 230px; }
  .contact__name { font-size: 26px; font-weight: 700; line-height: 1.1; }
  .contact__title { font-size: 14px; color: var(--ink-soft); margin-top: 4px; }
  .contact__rule { height: 1px; background: var(--rule-warm); margin: 8px 0 8px; }
  .contact__address { font-size: 13.5px; line-height: 1.4; color: var(--ink-soft); }
  .contact__list { list-style: none; margin-top: 12px; }
  .contact__item {
    display: flex; align-items: center; gap: 10px;
    font-size: 14px; color: var(--ink-soft); height: 21px;
  }
  .contact__icon { width: 11px; height: 11px; fill: var(--ink-soft); flex: none; }

  .company {
    position: absolute; left: 73px; right: 86px; top: 350px;
    display: flex; align-items: center; gap: 14px;
  }
  .company__line { flex: 1; height: 1px; background: var(--ink-soft); }
  .company__name { font-size: 26px; font-weight: 400; letter-spacing: 0.5px; }
</style>
</head>
<body>
<main class="canvas">
  <section class="card card--front" aria-label="Card front">
    <div class="wordmark">VEK 842 AS</div>
    <div class="divider"></div>
    <div class="contact">
      <div class="contact__name">Elena Varri</div>
      <div class="contact__title">Managing Director</div>
      <div class="contact__rule"></div>
      <div class="contact__address">Via Lucerna, 40128 Modena<br>( MO )P.IVA / C.FISC 04812736590</div>
      <div class="contact__rule"></div>
      <ul class="contact__list">
        <li class="contact__item">
          <svg class="contact__icon" viewBox="0 0 24 24"><path d="M6.6 10.8a15 15 0 0 0 6.6 6.6l2.2-2.2a1 1 0 0 1 1-.25 11.4 11.4 0 0 0 3.6.57 1 1 0 0 1 1 1V20a1 1 0 0 1-1 1A17 17 0 0 1 3 4a1 1 0 0 1 1-1h3.5a1 1 0 0 1 1 1c0 1.25.2 2.45.57 3.57a1 1 0 0 1-.25 1z"/></svg>
          000 0000 0000
        </li>
        <li class="contact__item">
          <svg class="contact__icon" viewBox="0 0 24 24"><path d="M2 5h20v14H2z M2 5l10 8 10-8" fill="none" stroke="currentColor" stroke-width="0"/><path d="M2 6v13h20V6l-10 7.5z"/><path d="M2 5h20l-10 7.5z"/></svg>
          info@vekmail.com
        </li>
        <li class="contact__item">
          <svg class="contact__icon" viewBox="0 0 24 24"><circle cx="12" cy="12" r="10" fill="none" stroke="#dcd6d0" stroke-width="2"/><ellipse cx="12" cy="12" rx="4" ry="10" fill="none" stroke="#dcd6d0" stroke-width="2"/><path d="M2 12h20" stroke="#dcd6d0" stroke-width="2"/></svg>
          www.vek842.com
        </li>
      </ul>
    </div>
  </section>

  <section class="card card--back" aria-label="Card back">
    <div class="wordmark">VEK 842 AS</div>
    <div class="company">
      <span class="company__line"></span>
      <span class="company__name">COMPANY NAME</span>
      <span class="company__line"></span>
    </div>
  </section>
</main>
</body>
</html>
```